Business Cards for Lean-Right-In

I need a business card that uses elements of my color pallet and book along with my company name and logo. The primary thing I'd like to have stand out is the word Lean-Right-In (i'd like to see this word in the orange from my pallet)
On the back of the card I want it to say Stop being Accountable, Be Lean-Right-In

Contact Information for Business Card

Q-Tier Fireside logo, Lean-Right-In, email - mpr@qtierfireside.example, phone 555-204-8817, Harborview | Northgate

Requirements
Nice to have
• colors from my color pallet

```html
<!DOCTYPE html>
<html lang="en">
<head>
<meta charset="utf-8">
<title>Lean-Right-In Business Card</title>
<link rel="stylesheet" href="https://fonts.googleapis.com/css2?family=Bebas+Neue&family=Poppins:wght@400;500&display=swap">
<style>
  :root {
    --backdrop: #d6d6d6;
    --navy: #21506f;
    --paper: #e6e6e8;
    --orange: #e0501e;
    --green: #6ab344;
    --partner-blue: #2a7fc0;
    --light-text: #e4e4e4;
  }
  * { margin: 0; padding: 0; box-sizing: border-box; }
  html, body {
    width: 1200px; height: 1101px; overflow: hidden;
    background: var(--backdrop);
  }
  .stage { position: relative; width: 1200px; height: 1101px; }
  .card {
    position: absolute; top: 277px; width: 302px; height: 511px;
  }
  .card-back { left: 246px; background: var(--navy); }
  .card-front { left: 641px; background: var(--paper); color: var(--navy); }

  .slogan {
    position: absolute; left: 0; right: 0; top: 202px;
    text-align: center;
    font-family: "Bebas Neue", sans-serif; font-weight: 400;
    font-size: 37px; line-height: 40px;
    color: var(--light-text);
  }
  .slogan .highlight { color: var(--orange); }
  .back-rule {
    position: absolute; left: 120px; top: 443px;
    width: 62px; height: 4px; background: var(--light-text);
  }

  .accent-bar {
    position: absolute; right: 0; top: 53px;
    width: 15px; height: 103px; background: var(--green);
  }
  .person-name {
    position: absolute; left: 28px; top: 58px;
    font-family: "Bebas Neue", sans-serif; font-weight: 400;
    font-size: 45px; line-height: 40px; letter-spacing: 1px;
  }
  .person-title {
    position: absolute; left: 28px; top: 141px;
    font-family: "Poppins", sans-serif; font-weight: 400; font-size: 15px;
  }
  .company-name {
    position: absolute; left: 28px; top: 219px;
    font-family: "Bebas Neue", sans-serif; font-weight: 400; font-size: 24px;
  }
  .contact-list {
    position: absolute; left: 28px; top: 253px; list-style: none;
    font-family: "Poppins", sans-serif; font-weight: 400; font-size: 13px;
  }
  .contact-list li {
    display: flex; align-items: center; gap: 8px; height: 27px;
    text-transform: uppercase; white-space: nowrap;
  }
  .contact-list svg { width: 15px; height: 15px; fill: var(--navy); flex: none; }

  .partner-marks {
    position: absolute; left: 40px; right: 26px; top: 672px; top: 395px;
    display: flex; justify-content: space-between; align-items: flex-end;
    font-family: "Poppins", sans-serif; font-weight: 500;
  }
  .partner {
    display: flex; flex-direction: column; align-items: center; gap: 6px;
    text-align: center;
  }
  .partner-primary { color: var(--partner-blue); font-size: 12px; line-height: 14px; width: 70px; }
  .partner-secondary { color: var(--navy); font-size: 19px; line-height: 22px; }
  .mark-circle { width: 26px; height: 26px; border-radius: 50%; background: var(--partner-blue); }
  .mark-square { width: 34px; height: 34px; background: var(--green); }
</style>
</head>
<body>
<main class="stage">
  <section class="card card-back" aria-label="Card back">
    <p class="slogan">Stop being<br>Accountable, be<br><span class="highlight">Lean-Right-In</span></p>
    <div class="back-rule"></div>
  </section>

  <section class="card card-front" aria-label="Card front">
    <div class="accent-bar"></div>
    <h1 class="person-name">John<br>Lastname</h1>
    <p class="person-title">DIRECTOR</p>
    <h2 class="company-name">Lean-Right-In</h2>
    <ul class="contact-list">
      <li>
        <svg viewBox="0 0 24 24" aria-hidden="true"><path d="M6.6 10.8a15.1 15.1 0 0 0 6.6 6.6l2.2-2.2a1 1 0 0 1 1-.25 11.4 11.4 0 0 0 3.6.57 1 1 0 0 1 1 1V20a1 1 0 0 1-1 1A17 17 0 0 1 3 4a1 1 0 0 1 1-1h3.5a1 1 0 0 1 1 1c0 1.25.2 2.46.57 3.6a1 1 0 0 1-.25 1z"/></svg>
        555-204-8817
      </li>
      <li>
        <svg viewBox="0 0 24 24" aria-hidden="true"><path d="M2 5h20v14H2zm2 2v.4l8 5.3 8-5.3V7zm0 2.8V17h16V9.8l-8 5.3z"/></svg>
        mpr@qtierfireside.example
      </li>
      <li>
        <svg viewBox="0 0 24 24" aria-hidden="true"><path d="M12 2a7 7 0 0 0-7 7c0 5.2 7 13 7 13s7-7.8 7-13a7 7 0 0 0-7-7zm0 9.5A2.5 2.5 0 1 1 12 6.5a2.5 2.5 0 0 1 0 5z"/></svg>
        Harborview | Northgate
      </li>
    </ul>
    <div class="partner-marks">
      <span class="partner partner-primary"><span class="mark-circle"></span>Q-Tier Fireside</span>
      <span class="partner partner-secondary"><span class="mark-square"></span>StepForward60</span>
    </div>
  </section>
</main>
</body>
</html>
```